Dufresne Roofing

Want a professional looking business card

Industry/Entity Type

Business

Contact Information for Business Card

Marc Dufresne ( Owner) marc@dufresneroofing-example.com, www.dufresneroofing-example.com, Adress: 4217 County road 42 Wendover,ON K0A3M1

```html
<!DOCTYPE html>
<html lang="en">
<head>
<meta charset="utf-8">
<title>Dufresne Roofing – Business Card</title>
<link rel="stylesheet" href="https://fonts.googleapis.com/css2?family=Arimo:wght@400;700&display=swap">
<style>
  :root {
    --navy: #1d4a8a;
    --navy-soft: #c9d5e6;
    --grey: #6a6a6a;
    --ink: #3c3c3c;
    --card: #f7f7f7;
    --stage: #2a2a2a;
  }
  * { margin: 0; padding: 0; box-sizing: border-box; }
  html, body { width: 1200px; height: 997px; overflow: hidden; }
  body {
    background: var(--stage);
    font-family: "Arimo", Arial, sans-serif;
    position: relative;
  }
  .card {
    position: absolute;
    width: 580px;
    height: 331px;
    background: var(--card);
    border-radius: 26px;
    overflow: hidden;
    box-shadow: 0 18px 40px rgba(0,0,0,.45);
  }
  .card--back { left: 60px; top: 90px; }
  .card--front { left: 560px; top: 500px; }

  .edge-tab {
    position: absolute;
    width: 12px;
    background: var(--navy);
  }
  .edge-tab--left { left: 0; border-radius: 0 6px 6px 0; }
  .edge-tab--right { right: 0; border-radius: 6px 0 0 6px; }
  .card--back .edge-tab--left { top: 170px; height: 130px; }
  .card--back .edge-tab--right { top: 30px; height: 120px; }
  .card--front .edge-tab--left { top: 40px; height: 250px; }
  .card--front .edge-tab--right { top: 40px; height: 110px; }

  .back-name {
    position: absolute;
    inset: 0;
    display: flex;
    align-items: center;
    justify-content: center;
    font-weight: 700;
    font-size: 62px;
    letter-spacing: 2px;
    color: var(--navy-soft);
    text-transform: uppercase;
    text-align: center;
    line-height: 1.05;
  }

  .brand {
    position: absolute;
    left: 48px;
    top: 120px;
    width: 230px;
    display: flex;
    align-items: center;
    gap: 10px;
  }
  .brand-mark {
    width: 14px; height: 14px;
    background: var(--navy);
    flex: none;
  }
  .brand-name {
    font-weight: 700;
    font-size: 27px;
    line-height: 1.1;
    color: var(--navy);
    text-transform: uppercase;
    letter-spacing: 1px;
  }
  .divider {
    position: absolute;
    left: 296px;
    top: 70px;
    width: 2px;
    height: 170px;
    background: linear-gradient(var(--card), var(--navy) 50%, var(--card));
  }
  .contact {
    position: absolute;
    left: 314px;
    top: 70px;
    width: 244px;
    color: var(--ink);
  }
  .contact-name {
    font-weight: 700;
    font-size: 16px;
    color: var(--navy);
    letter-spacing: .5px;
    text-transform: uppercase;
  }
  .contact-role { font-weight: 700; font-size: 12px; color: var(--grey); margin-top: 1px; }
  .contact-address { font-size: 12px; line-height: 1.3; margin-top: 14px; color: var(--navy); }
  .contact-lines { list-style: none; margin-top: 16px; }
  .contact-lines li {
    display: flex; align-items: center; gap: 8px;
    font-size: 11.5px; margin-bottom: 6px; color: var(--ink);
    white-space: nowrap;
  }
  .contact-icon { width: 14px; height: 14px; flex: none; }
  .contact-web {
    font-weight: 700; font-size: 10.5px; color: var(--navy);
    text-transform: uppercase; margin-top: 4px; white-space: nowrap;
  }
</style>
</head>
<body>
  <section class="card card--back" aria-label="Card back">
    <span class="edge-tab edge-tab--left"></span>
    <span class="edge-tab edge-tab--right"></span>
    <p class="back-name">Dufresne<br>Roofing</p>
  </section>

  <section class="card card--front" aria-label="Card front">
    <span class="edge-tab edge-tab--left"></span>
    <span class="edge-tab edge-tab--right"></span>

    <div class="brand">
      <span class="brand-mark"></span>
      <span class="brand-name">Dufresne Roofing</span>
    </div>

    <span class="divider"></span>

    <div class="contact">
      <p class="contact-name">Marc Dufresne</p>
      <p class="contact-role">Owner</p>
      <p class="contact-address">4217 County road 42<br>Wendover, ON K0A3M1</p>
      <ul class="contact-lines">
        <li>
          <svg class="contact-icon" viewBox="0 0 14 14" aria-hidden="true">
            <circle cx="7" cy="7" r="7" fill="#1d4a8a"/>
            <path d="M4.3 3.6c.4-.3.8-.2 1 .2l.6 1.1c.2.4 0 .7-.3.9l-.3.2c.3.9 1 1.6 1.9 2l.2-.3c.2-.3.6-.4.9-.2l1.1.6c.4.2.5.6.2 1-.5.8-1.3 1-2.3.5C5.7 9 4.9 8.1 4.3 6.7c-.4-1.1-.5-2.3 0-3.1z" fill="#fff"/>
          </svg>
          0435550198
        </li>
        <li>
          <svg class="contact-icon" viewBox="0 0 14 14" aria-hidden="true">
            <circle cx="7" cy="7" r="7" fill="#1d4a8a"/>
            <rect x="3.5" y="4.5" width="7" height="5" fill="none" stroke="#fff" stroke-width="1"/>
            <path d="M3.5 4.5 7 7.3l3.5-2.8" fill="none" stroke="#fff" stroke-width="1"/>
          </svg>
          marc@dufresneroofing-example.com
        </li>
      </ul>
      <p class="contact-web">www.dufresneroofing-example.com</p>
    </div>
  </section>
</body>
</html>
```